Window Graphics ‘Opening Soon’ for new Jewellery Boutique

We want to fully cover the shop window for a duration of 6 weeks whilst the refurbishment is going on. The window graphics should be cool, sexy and sophisticated. The graphics should include our company logo ‘THE COPPER LANTERN’ in Gills Sans Font. The shop will be an upmarket jewellery watch shop.

Target Market(s)

Jewellery customers

Industry/Entity Type

Jewellery

Colors

Designer to choose colors to be used in the design.

Requirements
Must have
• Must be loud graphics that catch your attention when walking past. I have provided a graphics example where the colour palette is black, white and shocking pink!
Nice to have
• The Boss is Back…. The Copper Lantern Proudly present a new masterpiece coming soon….

```html
<!DOCTYPE html>
<html lang="en">
<head>
<meta charset="utf-8">
<title>The Copper Lantern – Coming Soon Window Graphics</title>
<link href="https://fonts.googleapis.com/css2?family=Questrial&family=Montserrat:wght@600;700;800&display=swap" rel="stylesheet">
<style>
  :root {
    --pink: #ff0497;
    --ink: #111111;
    --shadow-grey: #8a8a8a;
    --panel-light: #ffffff;
    --panel-soft: #e9e9e9;
    --board: #ffffff;
    --canvas: #3a3a3a;
  }
  html, body {
    margin: 0; padding: 0;
    width: 1048px; height: 1200px;
    overflow: hidden;
    background: var(--canvas);
  }
  .window-board {
    position: absolute;
    left: 24px; top: 390px;
    width: 1000px; height: 421px;
    background: var(--board);
    border: 1px solid #cfcfcf;
    box-sizing: border-box;
  }
  .panel {
    position: absolute;
    top: 9px; height: 401px;
    overflow: hidden;
    background: linear-gradient(160deg, var(--panel-light) 0%, var(--panel-soft) 55%, var(--panel-light) 100%);
    border: 1px solid #9a9a9a;
    box-sizing: border-box;
  }
  .panel--left { left: 10px; width: 170px; }
  .panel--main { left: 197px; width: 615px; }
  .panel--right { left: 828px; width: 161px; }

  .dot {
    position: absolute;
    border-radius: 50%;
    background: var(--pink);
  }

  .brand-name {
    position: absolute;
    left: 0; width: 100%;
    text-align: center;
    font-family: "Questrial", sans-serif;
    font-size: 11.5px;
    color: var(--ink);
    letter-spacing: 0.2px;
  }

  /* left panel tagline */
  .tagline {
    position: absolute;
    left: 12px; top: 246px;
    width: 146px;
    text-align: center;
    font-family: "Montserrat", sans-serif;
    font-weight: 700;
    color: var(--ink);
  }
  .tagline__small {
    display: block;
    font-size: 11px;
    line-height: 14px;
    letter-spacing: 3px;
  }
  .tagline__large {
    display: block;
    font-size: 28px;
    line-height: 32px;
    letter-spacing: 1px;
  }

  .phone-pill {
    position: absolute;
    height: 17px;
    border: 1px solid var(--ink);
    border-radius: 9px;
    box-sizing: border-box;
    text-align: center;
    font-family: "Montserrat", sans-serif;
    font-weight: 700;
    font-size: 11.5px;
    line-height: 15px;
    letter-spacing: 1.5px;
    color: var(--ink);
  }
  .panel--left .phone-pill { left: 12px; top: 342px; width: 146px; }
  .panel--right .phone-pill { left: 7px; top: 342px; width: 147px; }

  /* right panel */
  .address {
    position: absolute;
    left: 25px; top: 248px;
    font-family: "Montserrat", sans-serif;
    font-weight: 700;
    font-size: 12px;
    line-height: 17px;
    color: var(--ink);
  }
  .address__pin {
    position: absolute;
    left: 25px; top: 234px;
  }

  /* main panel */
  .headline-name {
    position: absolute;
    left: 51px; top: 27px;
    font-family: "Questrial", sans-serif;
    font-size: 38px;
    line-height: 1;
    color: var(--ink);
    white-space: nowrap;
  }
  .headline-sub {
    position: absolute;
    left: 51px; top: 89px;
    font-family: "Montserrat", sans-serif;
    font-weight: 700;
    font-size: 18.8px;
    line-height: 1;
    color: var(--ink);
    white-space: nowrap;
  }
  .headline-big {
    position: absolute;
    left: 48px;
    font-family: "Montserrat", sans-serif;
    font-weight: 800;
    font-size: 94px;
    line-height: 1;
    letter-spacing: 0;
    color: var(--ink);
    text-shadow: 5px 4px 0 var(--shadow-grey);
    white-space: nowrap;
  }
  .headline-big--coming { top: 116px; }
  .headline-big--soon { top: 208px; }
  .web-address {
    position: absolute;
    left: 51px; top: 353px;
    font-family: "Montserrat", sans-serif;
    font-weight: 700;
    font-size: 12px;
    letter-spacing: 3.2px;
    color: var(--ink);
    white-space: nowrap;
  }
  .product-display {
    position: absolute;
    left: 362px; top: 190px;
    width: 218px; height: 211px;
    background:
      radial-gradient(ellipse 38% 34% at 40% 48%, rgba(201,160,74,0.85) 0%, rgba(201,160,74,0) 100%),
      radial-gradient(ellipse 30% 30% at 72% 40%, rgba(190,190,190,0.9) 0%, rgba(190,190,190,0) 100%),
      linear-gradient(180deg, rgba(240,240,240,0) 0%, #f1f1f1 75%, #e4e4e4 100%);
  }
</style>
</head>
<body>
  <main class="window-board">

    <section class="panel panel--left">
      <div class="dot" style="left:152px; top:-7px; width:174px; height:174px;"></div>
      <div class="dot" style="left:-95px; top:216px; width:174px; height:174px;"></div>
      <div class="brand-name" style="top:173px;">THE COPPER LANTERN</div>
      <div class="tagline">
        <span class="tagline__small">THE</span>
        <span class="tagline__large">BOSS</span>
        <span class="tagline__small">IS BACK</span>
      </div>
      <div class="phone-pill">0800 412 7730</div>
    </section>

    <section class="panel panel--main">
      <div class="dot" style="left:-1px; top:-14px; width:254px; height:254px;"></div>
      <div class="dot" style="left:573px; top:-40px; width:80px; height:80px;"></div>
      <div class="dot" style="left:581px; top:214px; width:118px; height:118px;"></div>
      <div class="dot" style="left:100px; top:340px; width:206px; height:206px;"></div>

      <div class="product-display" role="img" aria-label="Gold diver's watch and stacked diamond rings on a white podium with a gold ring arch and gold pearls"></div>

      <div class="headline-name">THE COPPER LANTERN</div>
      <div class="headline-sub">PROUDLY PRESENT A NEW MASTERPIECE</div>
      <div class="headline-big headline-big--coming">COMING</div>
      <div class="headline-big headline-big--soon">SOON</div>
      <div class="web-address">www.CopperLanternJewels.com</div>
    </section>

    <section class="panel panel--right">
      <div class="dot" style="left:-15px; top:-30px; width:60px; height:60px;"></div>
      <div class="dot" style="left:-5px; top:213px; width:120px; height:120px;"></div>
      <div class="brand-name" style="top:175px;">THE COPPER LANTERN</div>
      <svg class="address__pin" width="60" height="12" viewBox="0 0 60 12" aria-hidden="true">
        <circle cx="4" cy="3.5" r="2.6" fill="none" stroke="#111" stroke-width="1.2"/>
        <line x1="4" y1="6" x2="4" y2="10" stroke="#111" stroke-width="1.2"/>
        <line x1="0" y1="11" x2="8" y2="11" stroke="#111" stroke-width="1"/>
        <line x1="10" y1="11" x2="58" y2="11" stroke="#111" stroke-width="0.8"/>
      </svg>
      <div class="address">24 Harlow Street,<br>Mayfair, London<br>W1K 3QT</div>
      <div class="phone-pill">0800 412 7730</div>
    </section>

  </main>
</body>
</html>
```